Prospectus/Brochure Design for Partnerships Proposal

Require prospectus to be designed for partnerships packages with our company. The goal of this prospectus is to inspire partners to join Vintrel (our company).

Design should be creative and include colour and visual elements to make engaging.

Creativity with layout is encouraged as you see fit.

Company is Vintrel.com.au

Contents of brocuhure/prospectus in .pdf. Layout ok to play around with.

Target Market(s)

Startup, Small Business

Industry/Entity Type

Startup

Font styles to use
Sans Serif

Colors

Designer to choose colors to be used in the design.

Requirements
Must have
• Well designed, colour, visual elements, consistency through design with regards to spacing, typography and design elements
Should not have
• Too many colours, select a creative colour pallete and stick with it. Clipart or non vector images.

```html
<!DOCTYPE html>
<html lang="en">
<head>
<meta charset="utf-8">
<title>Vintrel – Partnership Prospectus</title>
<link href="https://fonts.googleapis.com/css2?family=Montserrat:wght@400;500;600;700&display=swap" rel="stylesheet">
<style>
  :root {
    --brand-blue: #1b9ad8;
    --brand-blue-deep: #1386c1;
    --ink: #2b2f33;
    --ink-soft: #4a4f55;
    --charcoal: #1d1f22;
    --paper: #f4f5f6;
    --paper-shade: #e4e6e8;
    --backdrop: #e9e9e9;
    --white: #ffffff;
    --photo-top-a: #7d8c99;
    --photo-top-b: #c9d2da;
    --photo-bottom-a: #5f7890;
    --photo-bottom-b: #b7c6d3;
  }
  * { box-sizing: border-box; margin: 0; padding: 0; }
  html, body { width: 1200px; height: 800px; overflow: hidden; background: var(--backdrop); }
  body { font-family: "Montserrat", Arial, sans-serif; }

  .canvas { position: relative; width: 1200px; height: 800px; overflow: hidden; }
  .spread {
    position: absolute; left: 50px; top: 30px; width: 1100px; height: 740px;
    display: flex; box-shadow: 0 6px 22px rgba(0,0,0,.18);
  }
  .page { position: relative; width: 550px; height: 740px; overflow: hidden; }
  .page-art { position: absolute; inset: 0; width: 100%; height: 100%; }

  /* Left page */
  .page--about { background: var(--brand-blue); }
  .about-copy {
    position: absolute; left: 40px; top: 215px; width: 320px; color: var(--white);
  }
  .about-title { font-size: 30px; font-weight: 700; letter-spacing: .2px; margin-bottom: 14px; }
  .about-copy p { font-size: 10.5px; line-height: 1.55; margin-bottom: 9px; font-weight: 400; }

  /* Right page */
  .page--partnering { background: linear-gradient(180deg, var(--paper) 0%, var(--paper-shade) 100%); }
  .brand-mark {
    position: absolute; right: 34px; top: 52px; font-size: 16px; font-weight: 700; color: var(--ink);
    letter-spacing: .4px;
  }
  .partner-copy { position: absolute; left: 36px; top: 74px; width: 478px; color: var(--ink-soft); }
  .partner-title {
    font-size: 24px; font-weight: 700; color: var(--brand-blue);
    text-decoration: underline; text-underline-offset: 4px; text-decoration-thickness: 2px;
    margin-bottom: 10px;
  }
  .partner-copy p { font-size: 10px; line-height: 1.5; margin-bottom: 8px; }
  .industry-list {
    display: grid; grid-template-columns: 1fr 1fr; column-gap: 20px; margin: 2px 0 10px;
    font-size: 10px; line-height: 1.45; color: var(--ink);
  }
  .industry-list ul { list-style: none; }
  .industry-list li { display: flex; align-items: center; gap: 6px; }
  .tick { width: 10px; height: 10px; flex: none; }
</style>
</head>
<body>
<div class="canvas">
  <div class="spread">

    <section class="page page--about">
      <svg class="page-art" viewBox="0 0 550 740">
        <defs>
          <linearGradient id="photoTop" x1="0" y1="0" x2="1" y2="1">
            <stop offset="0" stop-color="var(--photo-top-a)"/>
            <stop offset="1" stop-color="var(--photo-top-b)"/>
          </linearGradient>
          <linearGradient id="photoBottom" x1="0" y1="0" x2="1" y2="1">
            <stop offset="0" stop-color="var(--photo-bottom-a)"/>
            <stop offset="1" stop-color="var(--photo-bottom-b)"/>
          </linearGradient>
        </defs>
        <path role="img" aria-label="Photo of colleagues reviewing work on a laptop in a bright office"
              d="M170,0 H550 V450 C430,300 300,150 170,0 Z" fill="url(#photoTop)"/>
        <path d="M170,0 C300,150 430,300 550,450" fill="none" stroke="var(--white)" stroke-width="3"/>
        <polygon points="320,700 550,470 550,575" fill="var(--charcoal)"/>
        <polygon role="img" aria-label="Photo of a team meeting around a laptop"
                 points="230,740 550,575 550,740" fill="url(#photoBottom)"/>
      </svg>

      <div class="about-copy">
        <h1 class="about-title">Who is Vintrel</h1>
        <p>Vintrel was started by two founders in Sydney with one simple goal: to support entrepreneurs on their journey to success, offering the tools and knowledge they need to build lasting businesses.</p>
        <p>With our combined years of experience, we have helped startups grow through mentoring, events and digital resources that bring people and ideas together.</p>
        <p>Two months later we opened our first space, and it quickly became a home for founders wanting to share, learn and grow.</p>
        <p>Vintrel now hosts weekly events and workshops, helping thousands of members connect with the right experts and partners across Australia.</p>
        <p>Vintrel is growing rapidly as it continues to move towards its plan of becoming the leading startup community in the country.</p>
      </div>
    </section>

    <section class="page page--partnering">
      <svg class="page-art" viewBox="0 0 550 740">
        <defs>
          <linearGradient id="skyline" x1="0" y1="0" x2="0" y2="1">
            <stop offset="0" stop-color="#dfe2e5" stop-opacity="0"/>
            <stop offset="1" stop-color="#cfd3d7" stop-opacity=".7"/>
          </linearGradient>
          <linearGradient id="photoBottomRight" x1="0" y1="0" x2="1" y2="1">
            <stop offset="0" stop-color="var(--photo-bottom-b)"/>
            <stop offset="1" stop-color="var(--photo-bottom-a)"/>
          </linearGradient>
        </defs>
        <rect role="img" aria-label="Faint city skyline backdrop" x="0" y="260" width="550" height="480" fill="url(#skyline)"/>
        <path d="M0,14 C180,10 360,18 500,40" fill="none" stroke="var(--charcoal)" stroke-width="4"/>
        <polygon role="img" aria-label="Photo of a team meeting around a laptop, continued"
                 points="0,655 190,740 0,740" fill="url(#photoBottomRight)"/>
        <path d="M190,740 C300,715 440,690 550,655 V740 Z" fill="var(--brand-blue)"/>
      </svg>

      <div class="brand-mark">Vintrel</div>

      <div class="partner-copy">
        <h2 class="partner-title">Partnering with Vintrel</h2>
        <p>Vintrel is looking for partners in industries that maintain our ultimate goal of supporting everyday people in achieving their business aspirations.</p>
        <p>Being in the startup space and helping people in the process of creating businesses, we have always had entrepreneurs and startups approach us for paid services.</p>
        <p>We are looking for the following industries to partner with, who will benefit by leveraging our community and network to drive leads, build brand awareness and position themselves as thought leaders in their industries:</p>

        <div class="industry-list">
          <ul>
            <li><svg class="tick" viewBox="0 0 10 10"><path d="M1,5 L4,8 L9,2" fill="none" stroke="var(--brand-blue)" stroke-width="1.8"/></svg>App development</li>
            <li><svg class="tick" viewBox="0 0 10 10"><path d="M1,5 L4,8 L9,2" fill="none" stroke="var(--brand-blue)" stroke-width="1.8"/></svg>Web development</li>
            <li><svg class="tick" viewBox="0 0 10 10"><path d="M1,5 L4,8 L9,2" fill="none" stroke="var(--brand-blue)" stroke-width="1.8"/></svg>Accountants</li>
            <li><svg class="tick" viewBox="0 0 10 10"><path d="M1,5 L4,8 L9,2" fill="none" stroke="var(--brand-blue)" stroke-width="1.8"/></svg>PR agencies</li>
            <li><svg class="tick" viewBox="0 0 10 10"><path d="M1,5 L4,8 L9,2" fill="none" stroke="var(--brand-blue)" stroke-width="1.8"/></svg>Government</li>
            <li><svg class="tick" viewBox="0 0 10 10"><path d="M1,5 L4,8 L9,2" fill="none" stroke="var(--brand-blue)" stroke-width="1.8"/></svg>Sales Coaches</li>
            <li><svg class="tick" viewBox="0 0 10 10"><path d="M1,5 L4,8 L9,2" fill="none" stroke="var(--brand-blue)" stroke-width="1.8"/></svg>Government grant agencies</li>
          </ul>
          <ul>
            <li><svg class="tick" viewBox="0 0 10 10"><path d="M1,5 L4,8 L9,2" fill="none" stroke="var(--brand-blue)" stroke-width="1.8"/></svg>Graphics design</li>
            <li><svg class="tick" viewBox="0 0 10 10"><path d="M1,5 L4,8 L9,2" fill="none" stroke="var(--brand-blue)" stroke-width="1.8"/></svg>Law firms</li>
            <li><svg class="tick" viewBox="0 0 10 10"><path d="M1,5 L4,8 L9,2" fill="none" stroke="var(--brand-blue)" stroke-width="1.8"/></svg>Marketing</li>
            <li><svg class="tick" viewBox="0 0 10 10"><path d="M1,5 L4,8 L9,2" fill="none" stroke="var(--brand-blue)" stroke-width="1.8"/></svg>Digital Marketing Agencies</li>
            <li><svg class="tick" viewBox="0 0 10 10"><path d="M1,5 L4,8 L9,2" fill="none" stroke="var(--brand-blue)" stroke-width="1.8"/></svg>Pitching coaches</li>
            <li><svg class="tick" viewBox="0 0 10 10"><path d="M1,5 L4,8 L9,2" fill="none" stroke="var(--brand-blue)" stroke-width="1.8"/></svg>SEO</li>
          </ul>
        </div>

        <p>Our carefully thought out, strategic approach to connecting you with our community &amp; network will provide a platform to engage, educate and ultimately convert our audience into your clients.</p>
        <p>We plan to put on a series of videos and/or events explaining how business owners, entrepreneurs and startups can operate and optimise their businesses for success. With expertise and knowledge provided by our partners, we will provide much needed resources and support to our audience and startups who, based on our experiences, will find the processes out of their domain expertise and will ultimately employ the services of a professional in this instance – Our partners – You.</p>
        <p>The truth is once a startup company realises the intricacies of any one profession, they generally realise the advantages in both cost and time of having an industry expert perform the tasks for them.</p>
        <p>Leveraging our network, we have designed a partnership arrangement with the goal of generating you leads while positioning you and your company as thought leaders in your industry.</p>
      </div>
    </section>

  </div>
</div>
</body>
</html>
```